Business Card Design Project

Branding and Marketing Company

Target Market(s)

Lifestyle Brands. Velorra, Quince, Brisk Harbor

Industry/Entity Type

Business

Contact Information for Business Card

I'm looking for a sleek design that is simple yet stands out. I would like to see some embossed options and even metallic features. I am looking for a black and white theme business card. Our company font is Avenir (Regular, Italic, Bold) I would like to have just the logo and the following slogan on the back of card.CREATING THE NEXT BIG THING IN HEALTH & WELLNESS

```html
<!DOCTYPE html>
<html lang="en">
<head>
<meta charset="utf-8">
<title>Halden Business Cards</title>
<link rel="stylesheet" href="https://fonts.googleapis.com/css2?family=Nunito+Sans:wght@400;600;700&display=swap">
<style>
  :root {
    --stage: #1f1f1f;
    --card-white: #f4f4f4;
    --card-black: #0b0b0b;
    --ink: #2a2a2a;
    --ink-soft: #4a4a4a;
    --accent: #e8920f;
    --light-text: #e6e6e6;
  }
  * { box-sizing: border-box; margin: 0; padding: 0; }
  html, body {
    width: 1200px; height: 997px; overflow: hidden;
    background: var(--stage);
    font-family: "Nunito Sans", "Avenir", sans-serif;
  }
  .stage {
    position: relative; width: 1200px; height: 997px;
    display: flex; align-items: center; justify-content: center; gap: 60px;
  }
  .card {
    position: relative; width: 520px; height: 300px;
    border-radius: 18px; overflow: hidden;
    box-shadow: 0 18px 40px rgba(0,0,0,.55);
  }

  /* Front: logo and slogan */
  .card-front {
    background: linear-gradient(160deg, #ffffff 0%, var(--card-white) 60%, #dcdcdc 100%);
    display: flex; flex-direction: column; align-items: center; justify-content: center;
  }
  .brand {
    display: flex; align-items: center; gap: 12px;
    color: var(--ink); font-weight: 700; letter-spacing: 1px;
  }
  .brand-dot { width: 22px; height: 22px; border-radius: 50%; background: var(--ink); }
  .card-front .brand { font-size: 46px; }
  .slogan {
    position: absolute; bottom: 26px; left: 0; right: 0; text-align: center;
    font-size: 12px; letter-spacing: 1.4px; color: var(--ink-soft); font-weight: 600;
  }

  /* Back: contact details */
  .card-back { background: var(--card-black); }
  .back-top {
    position: absolute; top: 0; left: 0; right: 0; height: 132px;
    background: linear-gradient(180deg, #ffffff 0%, #e9e9e9 100%);
    display: flex; align-items: center; justify-content: center;
  }
  .card-back .brand { font-size: 34px; }
  .accent-rule { position: absolute; top: 132px; left: 0; right: 0; height: 4px; background: var(--accent); }
  .notch { position: absolute; top: 136px; left: 38px; }
  .reg-details {
    position: absolute; top: 148px; right: 24px; text-align: right;
    font-size: 10px; line-height: 1.45; color: var(--light-text);
  }
  .person { position: absolute; top: 160px; left: 24px; }
  .person-name { font-size: 21px; color: #ffffff; font-weight: 600; line-height: 1.1; }
  .person-role { font-size: 13px; color: var(--accent); font-weight: 600; }
  .contact-list { list-style: none; margin-top: 12px; }
  .contact-list li {
    display: flex; align-items: center; gap: 10px;
    font-size: 13px; color: var(--light-text); line-height: 1.55;
  }
  .contact-list svg { flex: none; }
  .web { margin-top: 4px; font-size: 13px; font-weight: 700; color: var(--accent); }
  .company {
    position: absolute; right: 24px; bottom: 58px; text-align: right;
  }
  .company-name { font-size: 14px; color: var(--accent); font-weight: 700; }
  .company-address { font-size: 12.5px; color: var(--light-text); }
</style>
</head>
<body>
<main class="stage">
  <section class="card card-front" aria-label="Card front">
    <div class="brand"><span class="brand-dot"></span>Halden</div>
    <p class="slogan">CREATING THE NEXT BIG THING IN HEALTH &amp; WELLNESS</p>
  </section>

  <section class="card card-back" aria-label="Card back">
    <div class="back-top">
      <div class="brand"><span class="brand-dot"></span>Halden</div>
    </div>
    <div class="accent-rule"></div>
    <svg class="notch" width="18" height="10" viewBox="0 0 18 10"><polygon points="0,0 18,0 9,10" fill="var(--accent)"/></svg>
    <p class="reg-details">ABN: 12 345 678 901<br>Level 2 (Cat 1 &amp; 4)</p>

    <div class="person">
      <p class="person-name">Jordan Ellery</p>
      <p class="person-role">Licensed Electrician</p>
      <ul class="contact-list">
        <li>
          <svg width="14" height="14" viewBox="0 0 14 14"><circle cx="7" cy="7" r="7" fill="var(--accent)"/><path d="M4.5 4 L6 4 L6.5 5.6 L5.7 6.3 Q6.5 7.8 7.8 8.4 L8.5 7.6 L10 8.1 L10 9.6 Q6 10 4.5 4Z" fill="#fff"/></svg>
          (02) 5550 1842
        </li>
        <li>
          <svg width="14" height="14" viewBox="0 0 14 14"><circle cx="7" cy="7" r="7" fill="var(--accent)"/><rect x="5" y="3.5" width="4" height="7" rx="0.8" fill="#fff"/></svg>
          0400 555 318
        </li>
        <li>
          <svg width="14" height="14" viewBox="0 0 14 14"><circle cx="7" cy="7" r="7" fill="var(--accent)"/><rect x="3.8" y="4.6" width="6.4" height="4.8" fill="#fff"/><path d="M3.8 4.6 L7 7.2 L10.2 4.6" stroke="var(--accent)" stroke-width="0.8" fill="none"/></svg>
          info@elleryelec.com.au
        </li>
      </ul>
      <p class="web">www.elleryelec.com.au</p>
    </div>

    <div class="company">
      <p class="company-name">J &amp; R Ellery Electrical Inc.</p>
      <p class="company-address">8/22 Harbour Rd, Millbrook 2040</p>
    </div>
  </section>
</main>
</body>
</html>
```